Website Redesign for NeedleForge.co.za – Bold, Modern & Professional Tattoo Supply Store (B2B ...

PLEASE DO NOT CONTACT US OUTSIDE PIXELBAZAAR.COM

We’re looking for a skilled and creative web designer to redesign NeedleForge.co.za, a leading tattoo equipment and supplies store based in South Africa. The business serves both B2B (tattoo studios, artists, wholesalers) and B2C (individual customers) markets.

The current website is outdated and lacks the modern, edgy look that reflects the tattoo industry. We want a fresh, bold, and professional design that appeals to both professional artists and retail customers — combining trust, style, and functionality.

About the Business:
Needle Forge supplies a wide range of tattoo-related products, including machines, needles, inks, hygiene supplies, and accessories. The company is well-established in the South African market and serves both individual tattoo artists and studios, as well as end customers looking for quality equipment.

The website must reflect the creative, bold, and artistic nature of the tattoo industry, while still being easy to navigate, fast, and conversion-focused.

What We’re Looking For:
A bold, modern design with a clear structure
Strong visual identity that reflects the tattoo culture — edgy, artistic, but still clean and professional
A layout that works for both B2B and B2C audiences
Clear product presentation and strong CTAs (Buy Now, Request Quote, Contact, etc.)
Fully responsive design (desktop + mobile)
Easy-to-navigate product categories and filters
Space for featured products, promotions, and artist-focused content
Integration of trust elements (payment icons, reviews, certifications, etc.)

Pages We Need Designed:
Homepage
Product detail page

Inspiration / Style Direction:
We’re looking for something with a strong personality, inspired by tattoo culture, but still clean and user-friendly. Think:

Dark theme with bold highlights (but open to light themes if well executed)
High-quality visuals and product imagery

Examples for inspiration:
GrimQuill.co.uk
Marlow QRV
Corvane Needle Supply
Moxie Salve

Deliverables:
Full desktop and mobile designs (Figma, XD, or PSD)
All design source files
Fonts, icons, and assets used
Clearly labeled layers and organized files
Ready for development handoff

Target Market(s)

NeedleForge.co.za targets both B2B and B2C customers in South Africa: B2B: Professional tattoo artists, studios, and wholesalers looking for high-quality, reliable equipment and bulk pricing. B2C: Individual customers, hobbyists, and beginners seeking safe, affordable tattoo supplies with guidance and support. The site should appeal to both experienced professionals and newcomers, combining a bold, authentic tattoo vibe with a clean, user-friendly shopping experience.

Industry/Entity Type

Tattoo Equipment & Supplies – E-commerce (B2B & B2C)

Number of Pages Required

2 page

Requirements
Must have
• Responsive design, bold tattoo-inspired visual style, clear navigation for B2B & B2C, strong product presentation, clear call-to-actions, trust elements (reviews, badges, payment icons), category filters & search, dedicated B2B/wholesale info page, speed-optimized layout, easy access to contact & support.
Should not have
• Overly complex animations, cluttered layout, generic stock images, too many fonts or colors, hidden navigation, auto-play videos or sounds, outdated visual styles, low-quality product images, confusing checkout process, unnecessary pop-ups.

```html
<!DOCTYPE html>
<html lang="en">
<head>
<meta charset="utf-8">
<title>Needle Forge – Tattoo Supplies</title>
<link href="https://fonts.googleapis.com/css2?family=Poppins:wght@400;500;600;700&family=Pinyon+Script&display=swap" rel="stylesheet">
<style>
:root{
  --cream:#f9f0e0;
  --cream-deep:#efe2c8;
  --ink:#1d1d1d;
  --muted:#8a8a8a;
  --line:#3a3a3a;
  --star:#f3a112;
  --white:#ffffff;
  --grey-btn:#c9c9c9;
}
*{margin:0;padding:0;box-sizing:border-box}
html,body{width:1200px;height:4605px;overflow:hidden}
body{position:relative;background:var(--white);font-family:"Poppins",sans-serif;color:var(--ink)}
.abs{position:absolute}
.script{font-family:"Pinyon Script",cursive;font-weight:400;color:var(--ink);white-space:nowrap;text-shadow:0 2px 3px rgba(0,0,0,.18)}
.heading{font-size:54px;line-height:80px}
.btn{position:absolute;display:flex;align-items:center;justify-content:center;font-size:15px;font-weight:500;border-radius:3px}
.btn-dark{background:var(--ink);color:var(--white)}
.btn-outline{border:1.5px solid var(--ink);color:var(--ink);background:transparent}
.band{position:absolute;left:0;width:1200px}
.cream{background:var(--cream)}
.deco{position:absolute;background:linear-gradient(180deg,rgba(175,160,135,.45),rgba(175,160,135,.18));border-radius:60px}

.brand{font-weight:700;font-size:24px;letter-spacing:1px}
.search{left:769px;top:50px;width:130px;height:19px;border:1px solid #ddd;border-radius:10px;background:#fff;font-size:6px;color:#999;padding:5px 10px}

.hero-title{left:148px;top:153px;font-size:74px;line-height:125px}
.hero-copy{left:150px;top:412px;width:350px;font-size:12px;line-height:20px}
.photo{position:absolute;border-radius:8px;box-shadow:0 8px 18px rgba(0,0,0,.3)}

.eyebrow{left:150px;top:770px;display:flex;align-items:center;gap:12px;font-size:15px;font-weight:500}
.eyebrow i{display:block;width:11px;height:24px;background:var(--ink)}
.cat-list{left:150px;top:930px;list-style:none}
.cat-list li{font-size:15px;color:var(--muted);height:48.5px}
.cat-list li.active{color:var(--ink);font-weight:500}
.prod{position:absolute;top:919px;width:210px}
.prod .pic{position:relative;height:215px}
.prod .row{display:flex;justify-content:space-between;align-items:center;margin-top:24px}
.prod .name{font-size:15px;font-weight:500}
.prod .price{font-size:20px;font-weight:600}
.prod .sub{font-size:12px;color:var(--muted);margin-top:6px}
.badge-new{position:absolute;left:16px;top:9px;width:54px;height:18px;background:#bdb5a7;color:#fff;font-size:10px;display:flex;align-items:center;justify-content:center}
.pager span{position:absolute;font-size:12px;color:var(--muted)}

.card{position:absolute;top:1575px;height:381px;background:#fff;border-radius:6px;box-shadow:0 4px 14px rgba(0,0,0,.08);overflow:hidden}
.card .pic{height:188px}
.card h4{font-size:14px;font-weight:600;margin:26px 14px 0}
.card p{font-size:10px;color:var(--muted);line-height:16px;margin:10px 14px 0}
.card .price{position:absolute;left:14px;top:283px;font-size:20px;font-weight:600}
.card .rate{position:absolute;right:14px;top:278px;text-align:right;font-size:9px;font-weight:500}
.card .stars{color:var(--star);font-size:13px;letter-spacing:3px}
.card .cart{position:absolute;left:14px;top:340px;font-size:14px;font-weight:600;text-decoration:underline}
.card .plus{position:absolute;right:14px;top:334px;width:28px;height:28px;background:var(--ink);color:#fff;border-radius:4px;font-size:20px;display:flex;align-items:center;justify-content:center;line-height:1}

.feat{position:absolute;top:2342px;width:220px;margin-left:-110px;text-align:center}
.feat .ico{width:64px;height:64px;margin:0 auto;border:3px solid var(--ink);border-radius:50%;display:flex;align-items:center;justify-content:center}
.feat .ico b{width:46px;height:46px;border-radius:50%;background:var(--ink);display:flex;align-items:center;justify-content:center}
.feat .dot{width:20px;height:20px;border-radius:50%;background:var(--ink);border:4px solid #bbb;margin:33px auto 0}
.feat h5{font-size:14px;font-weight:600;line-height:22px;margin-top:10px}
.feat p{font-size:10px;line-height:15px;margin-top:8px}

.story-copy{left:150px;top:3010px;width:410px;font-size:10px;line-height:19px;color:#666}
.ticks{left:150px;top:3130px;list-style:none}
.ticks li{font-size:12px;height:34px;display:flex;align-items:center;gap:12px;font-weight:500}
.ticks li i{width:12px;height:12px;border-radius:50%;background:var(--ink);display:flex;align-items:center;justify-content:center}

.review{position:absolute;width:292px;height:116px;background:#fff;border:1px solid #e6e6e6;border-radius:8px;box-shadow:0 4px 12px rgba(0,0,0,.08)}
.review .av{position:absolute;left:14px;top:24px;width:72px;height:72px;border-radius:50%;background:radial-gradient(circle at 50% 40%,#c9bba8,#5b534b)}
.review h6{position:absolute;left:96px;top:20px;font-size:15px;font-weight:500}
.review .q{position:absolute;right:18px;top:16px;font-size:22px;font-weight:700;line-height:1}
.review p{position:absolute;left:96px;top:48px;width:180px;font-size:9.5px;line-height:15px;color:#777}

.foot-brand{left:0;width:1200px;top:4010px;text-align:center;font-weight:700;font-size:80px;letter-spacing:4px}
.links{left:940px;top:4390px;list-style:none}
.links h6{font-size:15px;font-weight:600;margin-bottom:14px}
.links li{font-size:10px;height:19.5px}
.social{position:absolute;top:4485px;width:30px;height:30px;border-radius:50%;background:#fff;border:1px solid #ddd;display:flex;align-items:center;justify-content:center}
.social i{width:10px;height:10px;border-radius:50%;background:var(--ink);display:block}
</style>
</head>
<body>

<section class="band cream" style="top:0;height:676px">
  <div class="deco" role="img" aria-label="Faint tribal figure with tattoo machine decoration" style="left:-30px;top:170px;width:130px;height:480px"></div>
  <div class="deco" role="img" aria-label="Faint tribal figure decoration" style="left:1110px;top:200px;width:110px;height:460px"></div>
  <div class="abs" role="img" aria-label="Halftone dot texture" style="left:460px;top:520px;width:330px;height:156px;background:radial-gradient(ellipse at 60% 70%,rgba(29,29,29,.55),rgba(29,29,29,0) 65%)"></div>
</section>

<header>
  <div class="abs brand" style="left:150px;top:28px">NEEDLE FORGE</div>
  <div class="abs search">Search for Anything…</div>
  <svg class="abs" style="left:919px;top:52px" width="70" height="16" viewBox="0 0 70 16" fill="none" stroke="#1d1d1d" stroke-width="1.4">
    <path d="M1 2h3l2 8h8l2-6H5"/><circle cx="7" cy="13" r="1.2"/><circle cx="13" cy="13" r="1.2"/>
    <path d="M33 13l-5-5a3 3 0 0 1 5-4 3 3 0 0 1 5 4z"/>
    <circle cx="57" cy="5" r="3"/><path d="M51 14a6 5 0 0 1 12 0"/>
  </svg>
  <svg class="abs" style="left:1028px;top:52px" width="22" height="14" viewBox="0 0 22 14" stroke="#1d1d1d" stroke-width="2"><path d="M0 1h22M0 7h22M0 13h22"/></svg>
</header>

<h1 class="abs script hero-title">Bold Gear For<br>Bold Artists</h1>
<p class="abs hero-copy">Premium Tattoo Machines, Needles, Inks &amp; Supplies For Beginners To Pro Artists. Trusted By Studios Across South Africa.</p>
<a class="btn btn-dark" style="left:150px;top:500px;width:238px;height:40px">Explore Categories</a>
<a class="btn btn-outline" style="left:407px;top:500px;width:166px;height:40px">Shop Now</a>
<div class="photo" role="img" aria-label="Close-up of a detailed black and grey tattooed arm" style="left:640px;top:152px;width:265px;height:263px;background:radial-gradient(ellipse at 40% 35%,#c98a5a 0%,#6b4a38 30%,#2a2220 70%,#141111 100%)"></div>
<div class="photo" role="img" aria-label="Tattoo artist working on a client in the studio" style="left:792px;top:254px;width:258px;height:304px;background:radial-gradient(ellipse at 55% 45%,#b9aea2 0%,#6e645c 35%,#2e2a27 75%,#171514 100%)"></div>

<div class="abs eyebrow"><i></i>Categories</div>
<h2 class="abs script heading" style="left:150px;top:804px">Find Your Essential Tools.</h2>
<a class="btn btn-dark" style="left:810px;top:797px;width:240px;height:41px">View All Categories</a>
<ul class="abs cat-list">
  <li class="active">Tattoo Machines</li>
  <li>Needles &amp; Cartridges</li>
  <li>Inks</li>
  <li>Power Supplies</li>
  <li>Hygiene &amp; Protection</li>
  <li>Accessories</li>
</ul>
<div class="prod" style="left:350px"><div class="pic" role="img" aria-label="Black coil tattoo machine" style="background:radial-gradient(ellipse 30% 45% at 50% 50%,#3a3a3a,#8c8781 45%,var(--cream) 100%)"><span class="badge-new">New</span></div><div class="row"><span class="name">TATTOO MACHINE</span><span class="price">$20</span></div><div class="sub">Lorem ipsum dolosit amet</div></div>
<div class="prod" style="left:594px"><div class="pic" role="img" aria-label="Silver rotary tattoo machine" style="background:radial-gradient(ellipse 40% 35% at 50% 50%,#6d6d6d,#b5b0a8 45%,var(--cream) 100%)"></div><div class="row"><span class="name">TATTOO MACHINE</span><span class="price">$20</span></div><div class="sub">Lorem ipsum dolosit amet</div></div>
<div class="prod" style="left:838px"><div class="pic" role="img" aria-label="Gold coil tattoo machine" style="background:radial-gradient(ellipse 40% 40% at 50% 48%,#b08a22,#cfc08a 45%,var(--cream) 100%)"></div><div class="row"><span class="name">TATTOO MACHINE</span><span class="price">$20</span></div><div class="sub">Lorem ipsum dolosit amet</div></div>
<div class="pager">
  <div class="abs" style="left:731px;top:1255px;width:47px;height:33px;background:var(--grey-btn);display:flex;align-items:center;justify-content:center;color:#fff;font-size:18px">←</div>
  <div class="abs" style="left:808px;top:1260px;width:23px;height:23px;border-radius:50%;background:var(--ink);color:#fff;font-size:11px;display:flex;align-items:center;justify-content:center">1</div>
  <span style="left:860px;top:1263px">2</span><span style="left:907px;top:1263px">3</span><span style="left:955px;top:1263px">4</span>
  <div class="abs" style="left:1003px;top:1255px;width:47px;height:33px;background:var(--ink);display:flex;align-items:center;justify-content:center;color:#fff;font-size:18px">→</div>
</div>

<section class="band cream" style="top:1386px;height:753px">
  <div class="deco" role="img" aria-label="Faint tribal warrior decoration" style="left:-20px;top:120px;width:120px;height:560px"></div>
  <div class="deco" role="img" aria-label="Faint tattoo machine in hand decoration" style="left:1100px;top:120px;width:120px;height:560px"></div>
</section>
<h2 class="abs script heading" style="left:0;width:1200px;text-align:center;top:1458px">Top-Selling Gear Trusted By Pros.</h2>
<div class="card" style="left:150px;width:286px"><div class="pic" role="img" aria-label="Tattoo machines on a workbench" style="background:radial-gradient(ellipse at 45% 60%,#c08a5a 0%,#6a4a33 35%,#241d18 80%)"></div><h4>TOP-SELLING TATTOO MACHINES</h4><p>Premium Tattoo Machines, Needles, Inks &amp; Supplies For Beginners To Pro Artists.</p><div class="price">$20</div><div class="rate">4.5 &nbsp;Reating<div class="stars">★★★★★</div></div><a class="cart">ADD TO CART</a><span class="plus">+</span></div>
<div class="card" style="left:456px;width:286px"><div class="pic" role="img" aria-label="Bottles of tattoo ink in different colours" style="background:radial-gradient(ellipse at 55% 55%,#d9d2c8 0%,#7d8a8f 30%,#2a3033 70%,#141617 100%)"></div><h4>POPULAR INKS DIFFERENT COLORS</h4><p>Premium Tattoo Machines, Needles, Inks &amp; Supplies For Beginners To Pro Artists.</p><div class="price">$20</div><div class="rate">4.5 &nbsp;Reating<div class="stars">★★★★★</div></div><a class="cart">ADD TO CART</a><span class="plus">+</span></div>
<div class="card" style="left:762px;width:288px"><div class="pic" role="img" aria-label="Gloved hand holding a needle cartridge" style="background:radial-gradient(ellipse at 50% 50%,#5e7468 0%,#2d3b35 45%,#121815 100%)"></div><h4>NEEDLE CARTRIDGES</h4><p>Premium Tattoo Machines, Needles, Inks &amp; Supplies For Beginners To Pro Artists.</p><div class="price">$20</div><div class="rate">4.5 &nbsp;Reating<div class="stars">★★★★★</div></div><a class="cart">ADD TO CART</a><span class="plus">+</span></div>
<a class="btn btn-dark" style="left:502px;top:2013px;width:193px;height:41px">View Product</a>

<h2 class="abs script heading" style="left:0;width:1200px;text-align:center;top:2222px">Trusted By Artists Nationwide</h2>
<div class="abs" style="left:170px;top:2439px;width:860px;height:2px;background:var(--line)"></div>
<div class="feat" style="left:250px"><div class="ico"><b><svg width="22" height="22" viewBox="0 0 22 22" fill="none" stroke="#fff" stroke-width="2.2"><path d="M5 11l4 4 8-8"/></svg></b></div><div class="dot"></div><h5>HIGH-QUALITY<br>PRODUCTS</h5><p>Take A Vape Out Of Your Purse<br>Or Pick Up A Spray Bottle.</p></div>
<div class="feat" style="left:483px"><div class="ico"><b><svg width="24" height="20" viewBox="0 0 24 20" fill="none" stroke="#fff" stroke-width="2"><path d="M2 10l6-6 4 3 4-3 6 6-8 7z"/></svg></b></div><div class="dot"></div><h5>TRUSTED BY<br>PROFESSIONALS</h5><p>Take A Vape Out Of Your Purse Or<br>Pick Up A Spray Bottle.</p></div>
<div class="feat" style="left:715px"><div class="ico"><b><svg width="26" height="18" viewBox="0 0 26 18" fill="#fff"><rect x="1" y="2" width="15" height="10"/><path d="M17 5h5l3 4v3h-8z"/><circle cx="6" cy="14" r="2.5"/><circle cx="20" cy="14" r="2.5"/></svg></b></div><div class="dot"></div><h5>FAST &amp; RELIABLE<br>DELIVERY</h5><p>Take A Vape Out Of Your Purse<br>Or Pick Up A Spray Bottle.</p></div>
<div class="feat" style="left:949px"><div class="ico"><b><svg width="24" height="18" viewBox="0 0 24 18" fill="none" stroke="#fff" stroke-width="2"><rect x="1" y="1" width="22" height="16" rx="2"/><path d="M1 6h22M5 12h5"/></svg></b></div><div class="dot"></div><h5>SECURE<br>PAYMENTS</h5><p>Take A Vape Out Of Your Purse Or Pick<br>Up A Spray Bottle.</p></div>
<a class="btn btn-dark" style="left:500px;top:2591px;width:199px;height:41px">Discover More</a>

<section class="band cream" style="top:2727px;height:674px">
  <div class="deco" role="img" aria-label="Faint tribal shield figure decoration" style="left:1060px;top:60px;width:140px;height:600px"></div>
  <div class="abs" role="img" aria-label="Halftone dot texture" style="left:0;top:40px;width:160px;height:500px;background:radial-gradient(ellipse at 0% 50%,rgba(29,29,29,.35),rgba(29,29,29,0) 70%)"></div>
</section>
<h2 class="abs script" style="left:150px;top:2782px;font-size:54px;line-height:94px">Made For Artists. Loved<br>By Artists</h2>
<p class="abs story-copy">Lorem Ipsum Dolor Sit Amet Consectetur. Est Ipsum Lectus Eget Leo Penatibus Natoque Faucibus. At Blandit Duis Dolor Mauris Urna Tellus. Facilisis Vel Vitae Cras Lorem Vitae. Congue Commodo Tortor Amet Fermentum Sed Netus Id. Sit Sit Pellentesque Elementum Vulputate Viverra Cursus. Tempus Placerat Aliquam Magna Amet Et Feugiat Mauris Elementum. Sed Viverra Urna Enim Sem.</p>
<ul class="abs ticks">
  <li><i><svg width="8" height="8" viewBox="0 0 8 8" fill="none" stroke="#fff" stroke-width="1.5"><path d="M1.5 4l1.8 1.8L6.5 2.5"/></svg></i>Jahrzehnte Lang Umgab Es Ein Großes Mysterium</li>
  <li><i><svg width="8" height="8" viewBox="0 0 8 8" fill="none" stroke="#fff" stroke-width="1.5"><path d="M1.5 4l1.8 1.8L6.5 2.5"/></svg></i>Viele Jahrzehnte Lang Umgab Es Ein Großes</li>
  <li><i><svg width="8" height="8" viewBox="0 0 8 8" fill="none" stroke="#fff" stroke-width="1.5"><path d="M1.5 4l1.8 1.8L6.5 2.5"/></svg></i>Viele Umgab Es Ein Großes Mysterium</li>
  <li><i><svg width="8" height="8" viewBox="0 0 8 8" fill="none" stroke="#fff" stroke-width="1.5"><path d="M1.5 4l1.8 1.8L6.5 2.5"/></svg></i>Viele Jahrzehnte Lang Umgab Es Ein Großes Mysterium</li>
</ul>
<a class="btn btn-dark" style="left:150px;top:3285px;width:216px;height:41px">View Artist Story</a>
<div class="photo" role="img" aria-label="Tattooed artist in a dark shirt" style="left:592px;top:2914px;width:458px;height:412px;background:radial-gradient(ellipse at 55% 35%,#b8a48a 0%,#6c6157 30%,#2c2926 70%,#161514 100%);box-shadow:none"></div>

<h2 class="abs script" style="left:150px;top:3513px;font-size:54px;line-height:90px">What Artists Say<br>About Us</h2>
<p class="abs story-copy" style="top:3706px;width:395px;line-height:19px">Lorem Ipsum Dolor Sit Amet Consectetur. Varius Tincidunt In Parturient Tristique Enim Amet Lacus Quis Sed. Nulla Congue Purus In LacusLorem Ipsum Dolor Sit Amet Consectetur. Varius Tincidunt In Parturient Tristique Enim Amet Lacus Quis Sed. Nulla Congue Purus In Lacus.</p>
<a class="btn btn-dark" style="left:150px;top:3812px;width:170px;height:41px">View More</a>
<div class="review" style="left:758px;top:3494px"><div class="av" role="img" aria-label="Customer portrait"></div><h6>Dorian Vance</h6><span class="q">”</span><p>Wipe Or Spray On The Toilet Seat Or Any Surface Wipe Or Spray On The Toilet Seat.</p></div>
<div class="review" style="left:667px;top:3633px"><div class="av" role="img" aria-label="Customer portrait"></div><h6>Marisol Tate</h6><span class="q">”</span><p>Wipe Or Spray On The Toilet Seat Or Any Surface Wipe Or Spray On The Toilet Seat.</p></div>
<div class="review" style="left:758px;top:3771px"><div class="av" role="img" aria-label="Customer portrait"></div><h6>Quentin Hale</h6><span class="q">”</span><p>Wipe Or Spray On The Toilet Seat Or Any Surface Wipe Or Spray On The Toilet Seat.</p></div>

<footer class="band cream" style="top:3934px;height:671px">
  <div class="deco" role="img" aria-label="Faint tribal mask decoration" style="left:-10px;top:20px;width:170px;height:340px"></div>
  <div class="deco" role="img" aria-label="Faint tribal warrior decoration" style="left:1060px;top:20px;width:150px;height:340px"></div>
</footer>
<div class="abs foot-brand">NEEDLE FORGE</div>
<h2 class="abs script heading" style="left:0;width:1200px;text-align:center;top:4269px">Gear Up. Ink Bold. Needle Forge</h2>
<p class="abs" style="left:163px;top:4390px;font-size:12px;line-height:24px">Connecting you to dream properties worldwide,<br>with ease and expertise you can trust.</p>
<span class="social" style="left:165px"><i></i></span>
<span class="social" style="left:214px"><i></i></span>
<span class="social" style="left:262px"><i></i></span>
<div class="abs links">
  <h6>Quick Links</h6>
  <ul style="list-style:none">
    <li>Product Categories</li>
    <li>Contact Info</li>
    <li>Social Media</li>
    <li>Payments Icons</li>
    <li>Newsletter Signup</li>
  </ul>
</div>
<p class="abs" style="left:0;width:1200px;text-align:center;top:4566px;font-size:12px">Copyright © . All right reserved. 2025</p>

</body>
</html>
```